Travel Itinary for Premium segment

Hi all the best designers on Pixelbazaar,
We are a travel agency specialized on the premium segment that travels to New Zealand (www.ferntidejourneys.example – please check out the video on our home page to get a good idea of our brand in a few min). We have an exciting project available.
We want to create a branded itinerary template - based on a previous version that we have (please see links below) + market inspiration (from competitors, other luxury brands), and your creativity. Clients need to be able to view it on mobile as well. The template should represent luxury, elegance, wanderlust. This is the first document the customer will receive from us once the trip details are confirmed.
It should include:
- Front page
- Thank you page (thank you for choosing Fern Tide, with our founder’s photo, signature + a short message that I will send you once we confirm),
- Itinerary overview visual (beautiful pictures and short descriptions with focus on the locations summarizing the whole trip – see links below for inspiration)
- A more detailed itinerary overview (giving the client an overview of the activities per day - see competitor example below)
- Details about each day
- Contact info (this could be included on the thank you page or on the backside
Resources:
- Inspiration from competitor: https://files.sharebox.example/s/k4mq8z/Wandora%20Sample%20Itinerary%20-%2021%20DAYS.pdf
- This is the itinerary that should be laid out in the template:
https://docs.writepad.example/document/d/7hQpL2vXn9RtY4eWc8sKz3mB6fJa1uDg5oNi0CyTrE/edit
- this is the branded look and style; https://files.sharebox.example/s/r7tn2w/0753%20FTJ%20Presentation%2016by9%201.4-Brazil.indd
- Here are the Indesign files https://files.sharebox.example/sh/p2vc9d/BBBxkRtm4
- This is what the textured brand background should look like https://files.sharebox.example/s/h8yj3f/0753%20FTJ%20Itinerary%20Overview%201.7.pdf
- Fern Tide Fonts https://files.sharebox.example/s/z5nb6c/Arno%20Pro%20Bold%20Italic%20SmText.zip
https://files.sharebox.example/s/d3wq1x/Arno%20Pro%20Semibold%20Italic%20Display.zip
Are you up for this? Please confirm asap if you will be able to do it, by providing concepts. If we like the concepts we can go ahead.
Look forward to hearing from you.
Thanks,

```html
<!DOCTYPE html>
<html lang="en">
<head>
<meta charset="utf-8">
<title>Aldana Family 9 Day – Featuring</title>
<link rel="stylesheet" href="https://fonts.googleapis.com/css2?family=EB+Garamond:wght@400;600;700&display=swap">
<style>
  :root {
    --backdrop: #e9e4dc;
    --paper: #ffffff;
    --ink-dark: #2a2623;
    --ink-body: #6f5c4a;
    --rule: #8c8580;
    --badge: #58585a;
    --badge-text: #ffffff;
    --photo-rock: #b08a4a;
    --photo-sea: #7fb3bd;
    --photo-deck: #4a3a2c;
  }
  * { margin: 0; padding: 0; box-sizing: border-box; }
  html, body { width: 1200px; height: 1200px; overflow: hidden; }
  body { background: var(--backdrop); font-family: "EB Garamond", Georgia, serif; }

  .page {
    position: absolute; left: 197px; top: 30px;
    width: 806px; height: 1140px;
    background: var(--paper);
    box-shadow: 0 4px 18px rgba(0,0,0,.12);
  }
  .page-title {
    position: absolute; left: 38px; top: 86px; width: 622px;
    font-size: 32px; font-weight: 400; letter-spacing: .5px;
    color: var(--ink-dark); line-height: 1;
    padding-bottom: 4px; border-bottom: 1px solid var(--rule);
  }
  .brand-badge {
    position: absolute; left: 670px; top: 38px;
    width: 94px; height: 94px; border-radius: 50%;
    background: var(--badge);
    display: flex; align-items: center; justify-content: center;
  }
  .brand-badge span {
    color: var(--badge-text); font-size: 11px; letter-spacing: 2px;
    font-weight: 400; text-align: center; line-height: 1.2;
  }

  .feature {
    position: absolute; left: 38px; width: 730px; height: 209px;
  }
  .feature-photo {
    position: absolute; left: 0; top: 0; width: 237px; height: 209px;
    background: linear-gradient(180deg,
      var(--photo-rock) 0%, #8a7350 22%, var(--photo-sea) 34%,
      #a9ccd0 68%, #f1efea 80%, #e4ddd0 88%, var(--photo-deck) 92%, #2e241b 100%);
  }
  .feature-body { position: absolute; left: 247px; top: 0; width: 483px; }
  .feature-title {
    font-size: 19.5px; font-weight: 700; color: var(--ink-dark);
    line-height: 1; margin-top: 0;
  }
  .feature-text {
    margin-top: 13px;
    font-size: 14px; line-height: 20.4px; color: var(--ink-body);
    text-align: justify; column-count: 2; column-gap: 9px;
    height: 124px;
  }

  .footer {
    position: absolute; left: 38px; top: 1083px; width: 730px;
    border-top: 1px solid #c9c4bf; padding-top: 12px;
    color: var(--ink-body); font-size: 12.5px; line-height: 14px;
  }
  .footer strong { font-weight: 700; display: block; }
</style>
</head>
<body>
  <main class="page">
    <h1 class="page-title">FEATURING</h1>
    <div class="brand-badge"><span>FERN<br>TIDE</span></div>

    <section class="feature" style="top:172px">
      <div class="feature-photo" role="img" aria-label="Woman in white robe relaxing on a daybed beside turquoise sea and rocky hills"></div>
      <div class="feature-body">
        <h2 class="feature-title">Bay of Islands</h2>
        <p class="feature-text">The Bay of Islands is a subtropical microregion known for its stunning beauty &amp; history. For those that love beaches and water activities, it’s paradise. A three hour drive or 35 minute flight north of Auckland, the Bay of Islands encompasses 144 islands between Cape Brett and the Purerua Peninsula.</p>
      </div>
    </section>

    <section class="feature" style="top:399px">
      <div class="feature-photo" role="img" aria-label="Woman in white robe relaxing on a daybed beside turquoise sea and rocky hills"></div>
      <div class="feature-body">
        <h2 class="feature-title">Poor Knights</h2>
        <p class="feature-text">The Poor Knights Islands Marine Reserve is a protected area off the coast of the North Island of New Zealand. The reserve, established in 1981 and covering an area of 2400 ha, is administered by the Department of Conservation. It surrounds the Poor Knights Islands and adjacent rock stacks. It is one of the world’s ten most popular sites for scuba diving.</p>
      </div>
    </section>

    <section class="feature" style="top:626px">
      <div class="feature-photo" role="img" aria-label="Woman in white robe relaxing on a daybed beside turquoise sea and rocky hills"></div>
      <div class="feature-body">
        <h2 class="feature-title">Waikato</h2>
        <p class="feature-text">Situated in the heart of the North Island the diverse Hamilton &amp; Waikato region encompasses New Zealand’s fourth largest city, the country’s longest river, Hillside Movie Set, and the world famous Waitomo Caves with its glowworms and adventure tourism activities. Well-known for its nature-based tourism, outstanding beaches, underground adventure and off-the-beaten track experiences.</p>
      </div>
    </section>

    <section class="feature" style="top:853px">
      <div class="feature-photo" role="img" aria-label="Woman in white robe relaxing on a daybed beside turquoise sea and rocky hills"></div>
      <div class="feature-body">
        <h2 class="feature-title">Rotorua</h2>
        <p class="feature-text">Rotorua is a major destination for both domestic and international tourists; the tourism industry is by far the largest industry in the district. It is known for its geothermal activity, and features geysers – notably the Pohutu Geyser at Whakarewarewa – and hot mud pools. This thermal activity is sourced to the Rotorua caldera, on which the town lies. The Lakes of Rotorua are a collection of many lakes surrounding Rotorua.</p>
      </div>
    </section>

    <footer class="footer">
      <strong>ALDANA FAMILY 9 DAY</strong>
      QUEENSTOWN EXCLUSIVE TOUR PLAN
    </footer>
  </main>
</body>
</html>
```